Preisliste für Kosmetikinstitut
Zielgruppe
Ich benötige für mein Kosmetikinstitut eine Preisliste für die moderne Frau, aber auch Männer. Das Design sollte mein Logo enthalten. Farben des Designkonzepts einbauen.
A4 quer zum Falten, wie ein Heft, 1. Seite Preisliste mit logo, im Innenteil dann Anwendungen
Aufgabenstellung
Minimalistisch, ästhetisch, modern, edel
Kontaktdaten auf der Rückseite
LT Hautatelier
Lena Tessmar
Lindenstieg 17
83671 Ostermoor
EMail: lena@lt-hautatelier.de
Whatsapp: 0176 284 9017

```html
<!DOCTYPE html>
<html lang="de">
<head>
<meta charset="utf-8">
<title>Gesichtsbehandlungen – Preisliste</title>
<link href="https://fonts.googleapis.com/css2?family=Hind:wght@400;500;600&display=swap" rel="stylesheet">
<style>
  :root{
    --paper:#ffffff;
    --panel:#efedeb;
    --ink:#5f6b69;
    --ink-strong:#56625f;
    --photo-a:#d3d4d7;
    --photo-b:#b9a79b;
  }
  html,body{margin:0;padding:0;overflow:hidden;}
  body{width:1200px;height:848px;background:var(--paper);font-family:"Hind",sans-serif;color:var(--ink);}
  .spread{position:relative;width:1200px;height:848px;overflow:hidden;}
  .panel{position:absolute;left:67px;top:0;width:454px;height:848px;background:var(--panel);}
  .section-title{position:absolute;left:139px;top:144px;margin:0;font-weight:500;font-size:17.5px;line-height:22px;letter-spacing:.06em;color:var(--ink);}
  .section-rule{position:absolute;left:139px;top:177px;width:73px;height:1px;background:var(--ink);}
  .treatment{position:absolute;width:312px;}
  .col-left{left:139px;}
  .col-right{left:728px;}
  .treatment-head{position:relative;margin:0;font-weight:600;font-size:14px;line-height:20px;letter-spacing:.035em;color:var(--ink-strong);text-transform:uppercase;}
  .treatment-head .sub{display:block;}
  .treatment-head .sub-light{display:block;font-weight:400;}
  .price{position:absolute;top:0;font-weight:400;font-size:14px;letter-spacing:.03em;}
  .col-left .price{left:252px;}
  .col-right .price{left:251px;}
  .treatment-text{margin:5px 0 0;font-size:12.7px;line-height:17px;letter-spacing:.025em;}
  .justify{text-align:justify;}
  .photo{position:absolute;}
  .photo-portrait{left:504px;top:494px;width:168px;height:354px;background:linear-gradient(160deg,var(--photo-a) 0%,#c9bdb4 55%,var(--photo-b) 100%);}
  .photo-detail{left:678px;top:638px;width:168px;height:210px;background:linear-gradient(200deg,var(--photo-a) 0%,#c8bab0 60%,var(--photo-b) 100%);}
</style>
</head>
<body>
<main class="spread">
  <div class="panel"></div>

  <h1 class="section-title">GESICHTSBEHANDLUNGEN</h1>
  <div class="section-rule"></div>

  <section class="treatment col-left" style="top:194px">
    <h2 class="treatment-head">Express Facial Treatment<span class="price">€ 59,00</span></h2>
    <p class="treatment-text">Für alle, die wenig Zeit haben und trotzdem<br>ihre Haut auffrischen und revitalisieren wollen.<br>Reinigung, Enzympeeling, Serum, Maske,<br>Abschlusspflege; 35-45min</p>
  </section>

  <section class="treatment col-left" style="top:310px">
    <h2 class="treatment-head">Classic Facial Treatment<span class="sub">Klassische Gesichtsbehandlung</span><span class="price">€ 89,00</span></h2>
    <p class="treatment-text">Reinigung, Enzympeeling, Vapozon, Ausreinigung,<br>Augenbrauenkorrektur, Ampulle, Maske,individuelle<br>Abschlusspflege; 45-60min</p>
  </section>

  <section class="treatment col-left" style="top:429px">
    <h2 class="treatment-head">Clear Skin Treatment<span class="price">€ 89,00</span></h2>
    <p class="treatment-text justify">Die Haut wirkt ausgeglichener, Unreinheiten wird vorgebeugt, der Teint erhält Balance und kann sich beruhigen. Gleichzeitig wird die Haut durch die Hyaluronsäure vitalisiert und Falten und Fältchen kann entgegengewirkt werden. 50-60min</p>
  </section>

  <section class="treatment col-left" style="top:559px">
    <h2 class="treatment-head">Vasolis Treatment<span class="price">€ 89,00</span></h2>
    <p class="treatment-text">Hautrötungen und Couperose Erscheinungen werden<br>gelindert, die Gefäßwände werden gestärkt und das<br>Hautbild wirkt ausgeglichener, mögliche Irritationen<br>gehen zurück. Gleichzeitig sorgt die hochkonzent-<br>rierte Hyaluronsäure für Frische, Vitalität und Glätte;<br>50-60min</p>
  </section>

  <section class="treatment col-right" style="top:144px">
    <h2 class="treatment-head">Calmera Soft Treatment<span class="sub-light">(für die empfindliche, gereizte Haut)</span><span class="price">€ 79,00</span></h2>
    <p class="treatment-text justify">Entzündliche Prozesse können gemildert werden, gereizte Haut oder solche, die wenig verträgt, wird beruhigt. Irritationen können zurückgehen, die Haut erhält Balance.&nbsp; ca 50min</p>
  </section>

  <section class="treatment col-right" style="top:277px">
    <h2 class="treatment-head">Vitamin Soft Boost<span class="price">€ 79,00</span></h2>
    <p class="treatment-text">Vitamine sorgen für Power und Frische in und auf der Haut, die Widerstandskraft der Haut wird gestärkt. Die Faltentiefe kann gemildert werden. ca. 50min</p>
  </section>

  <section class="treatment col-right" style="top:376px">
    <h2 class="treatment-head">Anti-Age Advanced<span class="price">€ 99,00</span></h2>
    <p class="treatment-text justify">Die Haut wirkt insgesamt erfrischt, vitalisiert und gestrafft. Feine Linien und Fältchen werden reduziert.50-70min (je nach Peeling)</p>
  </section>

  <section class="treatment col-right" style="top:476px">
    <h2 class="treatment-head">Chemisches Peeling<span class="sub">(Oktober – April)</span><span class="price" style="top:20px">€ 89,00</span></h2>
    <p class="treatment-text justify">Professionelle Peelings können viele Problem-stellungen lindern, verbessern oder gar beheben. Dazu gehören die Zellerneuerung, Glättung der Hauttextur, Reduzierung von Pigmentflecken, Verbesserung von Akne.</p>
  </section>

  <div class="photo photo-portrait" role="img" aria-label="Porträtfoto einer Frau mit Sommersprossen, die Hände sanft am Gesicht"></div>
  <div class="photo photo-detail" role="img" aria-label="Ausschnitt desselben Porträts mit Händen an Wange und Hals"></div>
</main>
</body>
</html>
```